Melissa Dorvan Personal Business Card

I like orange. It's would better if my card have an orange background
Address: 5820 Halvers Lane #417
San Jose
California
US
Tel: 4085172049

Industry/Entity Type

Business

```html
<!DOCTYPE html>
<html lang="en">
<head>
<meta charset="utf-8">
<title>Melissa Dorvan — Business Card</title>
<link rel="stylesheet" href="https://fonts.googleapis.com/css2?family=Lobster&family=Open+Sans:wght@400&display=swap">
<style>
  :root {
    --card-orange: #fda731;
    --badge-white: #ffffff;
    --badge-line: #f9a42c;
    --name-dark: #333333;
    --name-orange: #ff8105;
    --text-dark: #222222;
  }
  html, body {
    margin: 0;
    padding: 0;
    overflow: hidden;
  }
  .card {
    width: 686px;
    height: 1200px;
    background: var(--card-orange);
    position: relative;
    overflow: hidden;
  }
  .badge {
    position: absolute;
    left: 0;
    top: 0;
    width: 686px;
    height: 1200px;
  }
  .badge-outer { fill: var(--badge-white); }
  .badge-rim { fill: var(--badge-line); }
  .badge-inner { fill: var(--badge-white); }
  .ring-text {
    font-family: "Open Sans", Arial, sans-serif;
    font-size: 25px;
    fill: var(--text-dark);
  }
  .ring-text--phone { font-size: 27px; letter-spacing: 0.5px; }
  .name {
    font-family: "Lobster", cursive;
    text-anchor: middle;
  }
  .name--first { fill: var(--name-dark); font-size: 86px; }
  .name--last { fill: var(--name-orange); font-size: 86px; }
</style>
</head>
<body>
<main class="card">
  <svg class="badge" viewBox="0 0 686 1200" width="686" height="1200" aria-label="Melissa Dorvan contact badge">
    <defs>
      <circle id="lobe-outer" cx="0" cy="-240" r="62"/>
      <circle id="lobe-rim" cx="0" cy="-214" r="58"/>
      <circle id="lobe-inner" cx="0" cy="-214" r="55.5"/>
      <path id="arc-address" d="M343,796 A196,196 0 1,1 343,404 A196,196 0 1,1 343,796"/>
      <path id="arc-phone" d="M343,378 A222,222 0 1,0 343,822 A222,222 0 1,0 343,378"/>
    </defs>

    <g class="badge-outer" transform="translate(343 600)">
      <circle cx="0" cy="0" r="250"/>
      <use href="#lobe-outer"/>
      <use href="#lobe-outer" transform="rotate(25.714)"/>
      <use href="#lobe-outer" transform="rotate(51.429)"/>
      <use href="#lobe-outer" transform="rotate(77.143)"/>
      <use href="#lobe-outer" transform="rotate(102.857)"/>
      <use href="#lobe-outer" transform="rotate(128.571)"/>
      <use href="#lobe-outer" transform="rotate(154.286)"/>
      <use href="#lobe-outer" transform="rotate(180)"/>
      <use href="#lobe-outer" transform="rotate(205.714)"/>
      <use href="#lobe-outer" transform="rotate(231.429)"/>
      <use href="#lobe-outer" transform="rotate(257.143)"/>
      <use href="#lobe-outer" transform="rotate(282.857)"/>
      <use href="#lobe-outer" transform="rotate(308.571)"/>
      <use href="#lobe-outer" transform="rotate(334.286)"/>
    </g>

    <g class="badge-rim" transform="translate(343 600)">
      <circle cx="0" cy="0" r="226"/>
      <use href="#lobe-rim"/>
      <use href="#lobe-rim" transform="rotate(25.714)"/>
      <use href="#lobe-rim" transform="rotate(51.429)"/>
      <use href="#lobe-rim" transform="rotate(77.143)"/>
      <use href="#lobe-rim" transform="rotate(102.857)"/>
      <use href="#lobe-rim" transform="rotate(128.571)"/>
      <use href="#lobe-rim" transform="rotate(154.286)"/>
      <use href="#lobe-rim" transform="rotate(180)"/>
      <use href="#lobe-rim" transform="rotate(205.714)"/>
      <use href="#lobe-rim" transform="rotate(231.429)"/>
      <use href="#lobe-rim" transform="rotate(257.143)"/>
      <use href="#lobe-rim" transform="rotate(282.857)"/>
      <use href="#lobe-rim" transform="rotate(308.571)"/>
      <use href="#lobe-rim" transform="rotate(334.286)"/>
    </g>

    <g class="badge-inner" transform="translate(343 600)">
      <circle cx="0" cy="0" r="224"/>
      <use href="#lobe-inner"/>
      <use href="#lobe-inner" transform="rotate(25.714)"/>
      <use href="#lobe-inner" transform="rotate(51.429)"/>
      <use href="#lobe-inner" transform="rotate(77.143)"/>
      <use href="#lobe-inner" transform="rotate(102.857)"/>
      <use href="#lobe-inner" transform="rotate(128.571)"/>
      <use href="#lobe-inner" transform="rotate(154.286)"/>
      <use href="#lobe-inner" transform="rotate(180)"/>
      <use href="#lobe-inner" transform="rotate(205.714)"/>
      <use href="#lobe-inner" transform="rotate(231.429)"/>
      <use href="#lobe-inner" transform="rotate(257.143)"/>
      <use href="#lobe-inner" transform="rotate(282.857)"/>
      <use href="#lobe-inner" transform="rotate(308.571)"/>
      <use href="#lobe-inner" transform="rotate(334.286)"/>
    </g>

    <text class="ring-text ring-text--address">
      <textPath href="#arc-address" startOffset="50%" text-anchor="middle">5820 Halvers Lane #417 • San Jose, California 95215 • USA</textPath>
    </text>
    <text class="ring-text ring-text--phone">
      <textPath href="#arc-phone" startOffset="50%" text-anchor="middle">||  Telephone: 408.517.2049  ||</textPath>
    </text>

    <text class="name name--first" x="345" y="572">Melissa</text>
    <text class="name name--last" x="352" y="662">Dorvan</text>
  </svg>
</main>
</body>
</html>
```